Stationary for Keeping Steady

we are in the process of creating a more professional image for our company Keeping Steady Paramedical Services. We have recently had a new logo and general brochure designed using artpitchhub and have been impressed by the quality of submissions.

We need:
- Letterhead (A4)
- Business Cards
- With compliments slips
- Email stationary

Letterhead information:
Address - 47 Wattlebrook Drive, Fernhollow Vic 3091
Phone - 1800 462 817
email - enquiries@keepsteady.com.au
Internet - www.keepsteady.com.au
ABN - 82 463 915 207
ACN - 264 871 035

Files need to be able to be edited in Illustrator CS2

Business Cards / with compliments slips / email stationary:
Double sided.
One side to have Name, Mobile number, company phone 1800462817, email, internet address

Files need to be able to be edited in Illustrator CS2 (except email stationary)

Our website is www.keepsteady.com.au for more information. Do not base designs on the website as it will eventually be revised.

Target Market(s)

Australian based businesses, government departments and schools. We specialise in corporate customers rather than public first aid course

Industry/Entity Type

Internet

Requirements
Must have
• Where applicable file to be editable in illustrator CS2 to allow future alterations.

```html
<!DOCTYPE html>
<html lang="en">
<head>
<meta charset="utf-8">
<title>Keeping Steady Stationery</title>
<link rel="stylesheet" href="https://fonts.googleapis.com/css2?family=Source+Sans+3:wght@400;600;700&display=swap">
<style>
  :root {
    --backdrop: #e6e7e8;
    --paper: #ffffff;
    --brand-red: #a31c22;
    --name-red: #d9473d;
    --mark: #d67466;
    --ink: #1a1a1a;
    --copy-grey: #5a5a5a;
    --edge: #2b2b2b;
    --frame: #9a9a9a;
  }
  * { box-sizing: border-box; margin: 0; padding: 0; }
  html, body { width: 1200px; height: 1041px; overflow: hidden; background: var(--backdrop); }
  body { font-family: "Source Sans 3", "Helvetica Neue", Arial, sans-serif; }

  .stage {
    position: absolute; left: 0; top: 0;
    width: 1073px; height: 931px;
    transform: scale(1.11836, 1.11815);
    transform-origin: 0 0;
  }
  .presentation-frame {
    position: absolute; left: 1px; top: 1px; width: 1071px; height: 929px;
    border: 1px solid var(--frame);
  }
  .piece { position: absolute; background: var(--paper); border: 1px solid var(--edge); overflow: hidden; }
  .piece svg.shape { position: absolute; left: 0; top: 0; }

  /* Brand lockup: name set in text, one colour, one weight, with a plain square */
  .brand { position: absolute; display: flex; align-items: center; }
  .brand-square { background: var(--mark); flex: none; }
  .brand-name { color: var(--name-red); font-weight: 700; line-height: 1; white-space: nowrap; }
  .brand-name .sub { display: block; }

  /* Letterhead */
  .letterhead { left: 462px; top: 66px; width: 599px; height: 853px; }
  .letterhead .brand { left: 176px; top: 32px; gap: 14px; }
  .letterhead .brand-square { width: 40px; height: 40px; }
  .letterhead .brand-name { font-size: 27px; }
  .letterhead .brand-name .sub { font-size: 12.5px; margin-top: 4px; }
  .letterhead-footer {
    position: absolute; left: 0; right: 0; top: 825px;
    text-align: center; color: #fff; font-size: 8.6px; font-weight: 600; white-space: nowrap;
  }
  .letterhead-footer .sep { margin: 0 3px; }

  /* Disc label */
  .disc { position: absolute; left: 52px; top: 16px; width: 365px; height: 365px; }
  .disc .brand { left: 6px; top: 151px; gap: 6px; }
  .disc .brand-square { width: 18px; height: 18px; }
  .disc .brand-name { font-size: 13px; }
  .disc .brand-name .sub { font-size: 6.5px; margin-top: 2px; }

  /* With compliments slip */
  .compliments { left: 18px; top: 305px; width: 656px; height: 313px; background: var(--paper); }
  .compliments .contact {
    position: absolute; left: 511px; top: 49px;
    font-size: 9.6px; font-weight: 700; color: var(--copy-grey); line-height: 17px; white-space: nowrap;
  }
  .compliments .brand { left: 11px; top: 190px; gap: 14px; }
  .compliments .brand-square { width: 50px; height: 50px; }
  .compliments .brand-name { font-size: 26px; }
  .compliments .brand-name .sub { font-size: 13px; margin-top: 4px; }
  .compliments .footer-band {
    position: absolute; left: 0; right: 0; bottom: 0; height: 36px;
    background: var(--brand-red); color: #fff; font-size: 12.5px; font-weight: 700;
    text-align: right; padding: 10px 26px 0 0;
  }

  /* Business card, portrait */
  .card-portrait { left: 12px; top: 663px; width: 144px; height: 258px; }
  .card-portrait .brand { left: 7px; top: 26px; gap: 6px; }
  .card-portrait .brand-square { width: 18px; height: 18px; }
  .card-portrait .brand-name { font-size: 13px; }
  .card-portrait .brand-name .sub { font-size: 6.3px; margin-top: 2px; }
  .card-portrait .contact {
    position: absolute; left: 20px; top: 127px;
    font-size: 8.6px; font-weight: 700; color: var(--copy-grey); line-height: 11.2px; white-space: nowrap;
  }

  /* Business card, landscape */
  .card-landscape { left: 180px; top: 778px; width: 258px; height: 144px; }
  .card-landscape .brand { left: 7px; top: 36px; gap: 6px; }
  .card-landscape .brand-square { width: 20px; height: 20px; }
  .card-landscape .brand-name { font-size: 13.5px; }
  .card-landscape .brand-name .sub { font-size: 6.4px; margin-top: 2px; }
  .card-landscape .contact {
    position: absolute; left: 160px; top: 68px;
    font-size: 7px; color: var(--ink); line-height: 8.6px; white-space: nowrap;
  }
  .card-landscape .contact .gap { height: 5px; }
  .card-landscape .phone {
    position: absolute; left: 5px; top: 129px; font-size: 7.2px; font-weight: 700; color: var(--ink);
  }
</style>
</head>
<body>
<div class="stage">
  <div class="presentation-frame"></div>

  <!-- Letterhead -->
  <section class="piece letterhead">
    <svg class="shape" width="599" height="853" viewBox="0 0 599 853" aria-hidden="true">
      <path d="M0 767 C 150 822, 400 840, 599 631 L599 853 L0 853 Z" fill="var(--brand-red)"/>
      <path d="M0 780 C 160 830, 420 842, 599 650" fill="none" stroke="#fff" stroke-width="1"/>
    </svg>
    <div class="brand">
      <span class="brand-square"></span>
      <span class="brand-name">Keeping Steady<span class="sub">Paramedical Services Pty Ltd</span></span>
    </div>
    <p class="letterhead-footer">47 Wattlebrook Drive, Fernhollow Vic 3091<span class="sep">|</span>1800 462 817<span class="sep">|</span>enquiries@keepsteady.com.au<span class="sep">|</span>www.keepsteady.com.au<span class="sep">|</span>ABN - 82 463 915 207</p>
  </section>

  <!-- Disc label -->
  <section class="disc">
    <svg width="365" height="365" viewBox="0 0 365 365" aria-hidden="true">
      <defs>
        <clipPath id="disc-face"><circle cx="182" cy="182" r="182"/></clipPath>
      </defs>
      <g clip-path="url(#disc-face)">
        <rect width="365" height="365" fill="var(--brand-red)"/>
        <circle cx="138" cy="154" r="204" fill="#fff"/>
        <circle cx="134" cy="150" r="193" fill="var(--brand-red)"/>
        <circle cx="131" cy="147" r="176" fill="#fff"/>
      </g>
      <circle cx="182" cy="182" r="181.5" fill="none" stroke="var(--edge)" stroke-width="1"/>
      <circle cx="182" cy="182" r="53" fill="var(--backdrop)" stroke="#888" stroke-width="0.8"/>
    </svg>
    <div class="brand">
      <span class="brand-square"></span>
      <span class="brand-name">Keeping Steady<span class="sub">Paramedical Services Pty Ltd</span></span>
    </div>
  </section>

  <!-- With compliments slip -->
  <section class="piece compliments">
    <div class="contact">
      47 Wattlebrook Drive,<br>
      Fernhollow Vic 3091<br>
      1800 462 817<br>
      enquiries@keepsteady.com.au<br>
      www.keepsteady.com.au<br>
      ABN - 82 463 915 207
    </div>
    <div class="brand">
      <span class="brand-square"></span>
      <span class="brand-name">Keeping Steady<span class="sub">Paramedical Services Pty Ltd</span></span>
    </div>
    <div class="footer-band">With Compliments</div>
  </section>

  <!-- Business card, portrait -->
  <section class="piece card-portrait">
    <svg class="shape" width="144" height="258" viewBox="0 0 144 258" aria-hidden="true">
      <path d="M0 205 C 30 235, 90 246, 144 246 L144 258 L0 258 Z" fill="var(--brand-red)"/>
      <path d="M0 214 C 35 240, 95 250, 144 250" fill="none" stroke="#fff" stroke-width="0.8"/>
    </svg>
    <div class="brand">
      <span class="brand-square"></span>
      <span class="brand-name">Keeping Steady<span class="sub">Paramedical Services Pty Ltd</span></span>
    </div>
    <div class="contact">
      47 Wattlebrook Drive,<br>
      Fernhollow Vic 3091<br>
      1800 462 817<br>
      enquiries@keepsteady.com.au<br>
      www.keepsteady.com.au<br>
      ABN - 82 463 915 207
    </div>
  </section>

  <!-- Business card, landscape -->
  <section class="piece card-landscape">
    <svg class="shape" width="258" height="144" viewBox="0 0 258 144" aria-hidden="true">
      <path d="M0 0 L258 0 L258 58 C 200 20, 100 8, 0 18 Z" fill="var(--brand-red)"/>
      <path d="M0 20 C 100 10, 200 22, 258 62 L258 70 C 200 30, 100 16, 0 22 Z" fill="var(--ink)"/>
      <path d="M0 19 C 100 9, 200 21, 258 60" fill="none" stroke="#fff" stroke-width="0.8"/>
    </svg>
    <div class="brand">
      <span class="brand-square"></span>
      <span class="brand-name">Keeping Steady<span class="sub">Paramedical Services Pty Ltd</span></span>
    </div>
    <div class="contact">
      47 Wattlebrook Drive,<br>
      Fernhollow Vic 3091
      <div class="gap"></div>
      ACN - 264 871 035<br>
      ABN - 82 463 915 207
      <div class="gap"></div>
      www.keepsteady.com.au<br>
      enquiries@keepsteady.com.au
    </div>
    <div class="phone">1800 462 817</div>
  </section>
</div>
</body>
</html>
```